out of the box Business Card Design for a Manufacturer / Distributor

We are a manufarturer and distributor of products.
the company name is VORTANI (Pic attached)

the picture is NOT a must have on the business Card.

the Business Card should look really professional and/or special, so out of the box thinking is welcome.

there should be 2 Adresses on the Business Card for Main and Branch Office.
Email Adress, homepage, Name is required
NO Phone Number

Our working field:
Private Labeling
high Quality Production
direct distribution
warehousing
trademark registration
legal support

Main Office:
Kornblumenweg 14
08352 Lindenau
Germany

Branch Office:
Daska Lane
Rahimabad
Pakistan

Names:
Lukas Feldhaus (Owner)
Imran Qureshi (Owner)

Email:
lukas@vortani-example.com
imran@vortani-example.com

homepage:
vortani-example.com

Industry/Entity Type

Manufacturer Distributer

Contact Information for Business Card

Vortani

Requirements
Must have
• Names, both office Adresses, email, homepage
Should not have
• Phone Number

```html
<!DOCTYPE html>
<html lang="en">
<head>
<meta charset="utf-8">
<title>Vortani Business Card</title>
<link href="https://fonts.googleapis.com/css2?family=Open+Sans:wght@300;400;600;700&display=swap" rel="stylesheet">
<style>
  :root {
    --bg: #d4d5d7;
    --card-dark: #2e2e2e;
    --card-light: #ffffff;
    --ink-dark: #2b2b2b;
    --ink-light: #ffffff;
    --rule: #2b2b2b;
    --watermark: #efefef;
  }
  * { box-sizing: border-box; margin: 0; padding: 0; }
  html, body {
    width: 1200px; height: 804px; overflow: hidden;
    background: var(--bg);
    font-family: "Open Sans", Arial, sans-serif;
  }
  .stage {
    width: 1200px; height: 804px;
    display: flex; align-items: center; justify-content: center; gap: 40px;
  }
  .card {
    width: 540px; height: 309px;
    border-radius: 22px;
    position: relative; overflow: hidden;
    box-shadow: 0 6px 18px rgba(0,0,0,.18);
  }

  /* Front: dark side */
  .card--front { background: var(--card-dark); color: var(--ink-light); }
  .front__brand {
    position: absolute; top: 54px; left: 0; right: 0;
    display: flex; align-items: center; justify-content: center; gap: 14px;
  }
  .brand-dot { width: 22px; height: 22px; border-radius: 50%; background: currentColor; }
  .brand-name { font-weight: 300; font-size: 52px; letter-spacing: 2px; line-height: 1; }
  .front__web {
    position: absolute; top: 122px; left: 0; right: 0; text-align: center;
    font-weight: 700; font-size: 15px; letter-spacing: 2px;
  }
  .fields { position: absolute; top: 172px; left: 0; right: 0; }
  .fields__title {
    text-align: center; font-weight: 700; font-size: 15px; letter-spacing: 1.5px;
    margin-bottom: 12px;
  }
  .fields__list {
    list-style: none;
    display: grid; grid-template-columns: 190px 210px; column-gap: 30px; row-gap: 4px;
    justify-content: center;
    font-size: 12.5px; letter-spacing: 1px;
  }
  .fields__list li { display: flex; align-items: center; gap: 8px; }
  .bullet { width: 8px; height: 8px; border-radius: 50%; background: var(--ink-light); flex: none; }

  /* Back: light side */
  .card--back { background: var(--card-light); color: var(--ink-dark); }
  .back__watermark {
    position: absolute; right: -70px; bottom: -100px;
    width: 190px; height: 190px; border-radius: 50%;
    border: 26px solid var(--watermark);
  }
  .back__brand {
    position: absolute; top: 34px; left: 0; right: 0;
    display: flex; align-items: center; justify-content: center; gap: 14px;
  }
  .back__brand .brand-name { font-size: 46px; }
  .back__divider {
    position: absolute; left: 270px; top: 132px; width: 1px; height: 140px;
    background: var(--rule);
  }
  .contacts { position: absolute; left: 44px; top: 130px; width: 216px; }
  .contact { margin-bottom: 12px; }
  .contact__name {
    display: flex; align-items: center; gap: 6px;
    font-weight: 700; font-size: 14px; letter-spacing: 1px;
  }
  .contact__role { font-size: 11px; letter-spacing: 1px; padding-left: 18px; }
  .contact__mail {
    display: flex; align-items: center; gap: 6px;
    font-size: 11px; font-weight: 300; letter-spacing: .8px;
  }
  .offices { position: absolute; left: 292px; top: 138px; width: 230px; z-index: 1; }
  .office { margin-bottom: 10px; }
  .office__title { font-weight: 700; font-size: 14px; letter-spacing: 1px; }
  .office__addr { font-size: 11px; font-weight: 600; letter-spacing: .6px; line-height: 1.4; }
  .icon { width: 12px; height: 12px; flex: none; }
</style>
</head>
<body>
<main class="stage">

  <section class="card card--front">
    <div class="front__brand">
      <span class="brand-dot"></span>
      <span class="brand-name">VORTANI</span>
    </div>
    <div class="front__web">www.vortani-example.com</div>
    <div class="fields">
      <h2 class="fields__title">Our Working Field:</h2>
      <ul class="fields__list">
        <li><span class="bullet"></span>Private Labeling</li>
        <li><span class="bullet"></span>High Quality Production</li>
        <li><span class="bullet"></span>Direct Distribution</li>
        <li><span class="bullet"></span>Warehousing</li>
        <li><span class="bullet"></span>Legal Support</li>
        <li><span class="bullet"></span>Trademark Registration</li>
      </ul>
    </div>
  </section>

  <section class="card card--back">
    <div class="back__watermark" aria-hidden="true"></div>
    <div class="back__brand">
      <span class="brand-dot"></span>
      <span class="brand-name">VORTANI</span>
    </div>

    <div class="contacts">
      <div class="contact">
        <div class="contact__name">
          <svg class="icon" viewBox="0 0 12 12" aria-hidden="true"><circle cx="6" cy="4" r="2.5" fill="none" stroke="#2b2b2b" stroke-width="1"/><path d="M1.5 11.5c0-2.8 2-4.2 4.5-4.2s4.5 1.4 4.5 4.2z" fill="none" stroke="#2b2b2b" stroke-width="1"/></svg>
          Lukas Feldhaus
        </div>
        <div class="contact__role">Owner</div>
        <div class="contact__mail">
          <svg class="icon" viewBox="0 0 12 12" aria-hidden="true"><circle cx="6" cy="6" r="6" fill="#2b2b2b"/><rect x="3" y="4" width="6" height="4" fill="none" stroke="#fff" stroke-width=".8"/><path d="M3 4l3 2.2L9 4" fill="none" stroke="#fff" stroke-width=".8"/></svg>
          lukas@vortani-example.com
        </div>
      </div>
      <div class="contact">
        <div class="contact__name">
          <svg class="icon" viewBox="0 0 12 12" aria-hidden="true"><circle cx="6" cy="4" r="2.5" fill="none" stroke="#2b2b2b" stroke-width="1"/><path d="M1.5 11.5c0-2.8 2-4.2 4.5-4.2s4.5 1.4 4.5 4.2z" fill="none" stroke="#2b2b2b" stroke-width="1"/></svg>
          Imran Qureshi
        </div>
        <div class="contact__role">Owner</div>
        <div class="contact__mail">
          <svg class="icon" viewBox="0 0 12 12" aria-hidden="true"><circle cx="6" cy="6" r="6" fill="#2b2b2b"/><rect x="3" y="4" width="6" height="4" fill="none" stroke="#fff" stroke-width=".8"/><path d="M3 4l3 2.2L9 4" fill="none" stroke="#fff" stroke-width=".8"/></svg>
          imran@vortani-example.com
        </div>
      </div>
    </div>

    <div class="back__divider" aria-hidden="true"></div>

    <div class="offices">
      <div class="office">
        <div class="office__title">Main Office:</div>
        <div class="office__addr">Kornblumenweg 14, 08352 Lindenau<br>Germany</div>
      </div>
      <div class="office">
        <div class="office__title">Branch Office:</div>
        <div class="office__addr">Daska Lane, Rahimabad, Pakistan</div>
      </div>
    </div>
  </section>

</main>
</body>
</html>
```